Marbury Church Winter Cantata 2013

Create a 18x22 inch poster for an upcoming church concert event with the following details:
Theme: Jesus Is Coming Again
Date:12/21/13 Time: 10:40am
Featuring the Choirs of the Marbury Church and special guests.
Marbury FBC Church
514-36 92nd Street,
Laurelton, NY 11287
Pastor Delton K. Fairweather
The target audience is predominantly african-american
The concert theme has been changed to: "Jesus The Light of the World"
Church

```html
<!DOCTYPE html>
<html lang="en">
<head>
<meta charset="utf-8">
<title>Marbury Church Winter Cantata 2013 – Jesus the Light of the World</title>
<link rel="stylesheet" href="https://fonts.googleapis.com/css2?family=Rye&family=Lobster&family=Arvo:wght@700&family=Source+Sans+3:ital,wght@0,400;0,700;1,400&display=swap">
<style>
  :root {
    --page: #ececec;
    --night-top: #1a2260;
    --night-mid: #1b2478;
    --night-low: #0a0d24;
    --ground: #050507;
    --gold: #fdb515;
    --gold-deep: #e8a30f;
    --magenta: #c4199c;
    --white: #ffffff;
    --lamp: #f2d27a;
  }
  * { margin: 0; padding: 0; box-sizing: border-box; }
  html, body { width: 1200px; height: 1000px; overflow: hidden; }
  body { background: var(--page); position: relative; }

  .poster {
    position: absolute; left: 210px; top: 0;
    width: 780px; height: 1000px; overflow: hidden;
    background: var(--ground);
  }
  .night-sky {
    position: absolute; inset: 0;
    background: linear-gradient(180deg, var(--night-top) 0%, var(--night-mid) 40%, #141c5c 58%, var(--night-low) 72%, var(--ground) 82%);
  }
  .nativity-scene {
    position: absolute; left: 280px; top: 728px; width: 220px; height: 120px;
    border-radius: 6px;
    background: linear-gradient(180deg, #2a2a2e 0%, #3b3320 30%, var(--lamp) 55%, #1a1710 100%);
    opacity: .9;
  }

  .ornament {
    position: absolute; left: 285px; width: 210px; height: 40px;
    border-radius: 20px; background: var(--magenta);
  }
  .ornament--top { top: 132px; }
  .ornament--bottom { top: 432px; }

  .title {
    position: absolute; left: 0; right: 0; top: 192px;
    text-align: center;
    font-family: "Rye", serif; font-size: 136px; line-height: 1;
    color: var(--gold);
    text-shadow: 6px 6px 0 var(--magenta);
  }

  .ribbon {
    position: absolute; left: 135px; top: 345px; width: 530px; height: 70px;
    border-radius: 4px;
    background: linear-gradient(90deg, var(--gold-deep), var(--gold) 15%, var(--gold) 85%, var(--gold-deep));
  }
  .ribbon-text {
    position: absolute; left: 135px; top: 352px; width: 530px;
    text-align: center;
    font-family: "Lobster", cursive; font-size: 44px; line-height: 56px; color: var(--magenta);
  }

  .featuring {
    position: absolute; left: 0; right: 0; top: 508px; text-align: center;
    font-family: "Source Sans 3", sans-serif; font-style: italic; font-size: 25px;
    color: var(--gold);
  }
  .performers {
    position: absolute; left: 0; right: 0; top: 540px; text-align: center;
    font-family: "Arvo", serif; font-weight: 700; font-size: 30px; line-height: 40px;
    color: var(--white);
  }
  .schedule {
    position: absolute; left: 0; right: 0; top: 664px; text-align: center;
    font-family: "Source Sans 3", sans-serif; font-size: 22px; color: var(--gold);
  }
  .schedule strong { color: var(--white); font-weight: 700; }
  .schedule .gap { display: inline-block; width: 44px; }

  .venue {
    position: absolute; left: 0; right: 0; top: 896px; text-align: center;
    font-family: "Source Sans 3", sans-serif; font-size: 23px; color: var(--white);
  }
  .pastor {
    position: absolute; left: 0; right: 0; top: 936px; text-align: center;
    font-family: "Arvo", serif; font-weight: 700; font-size: 18px; color: var(--gold);
  }
</style>
</head>
<body>
  <main class="poster">
    <div class="night-sky" role="img" aria-label="Starry night sky with a bright star sending a beam of light down, faint musical notes"></div>

    <div class="ornament ornament--top" role="img" aria-label="Magenta scroll ornament"></div>
    <h1 class="title">JESUS</h1>

    <div class="ribbon" role="img" aria-label="Gold ribbon banner"></div>
    <p class="ribbon-text">the Light of the World</p>
    <div class="ornament ornament--bottom" role="img" aria-label="Magenta scroll ornament"></div>

    <p class="featuring">Featuring:</p>
    <h2 class="performers">The Choirs of the Marbury Church<br>and Special Guests</h2>
    <p class="schedule">Date: <strong>12/21/13</strong><span class="gap"></span>Time: <strong>10:40am</strong></p>

    <div class="nativity-scene" role="img" aria-label="Lit stable at night with the nativity scene in silhouette"></div>

    <p class="venue">Marbury FBC Church 514-36 92nd Street, Laurelton, NY 11287</p>
    <p class="pastor">Pastor Delton K. Fairweather</p>
  </main>
</body>
</html>
```